New Business Cards / Logo update

Logo:
can be updated but wanted pricing

New Business Cards:
take our existing business cards and upgrade them from a design perspective. We have two versions
Inside sales team does not have a cell phone and they use an appointment back slot.
Outside project managers and leadership uses a slogan backing and will have cell phones.

```html
<!DOCTYPE html>
<html lang="en">
<head>
<meta charset="utf-8">
<title>Keystone Carpet + Flooring — Business Cards</title>
<link href="https://fonts.googleapis.com/css2?family=Bitter:wght@400;500&family=Arimo:wght@400;700&display=swap" rel="stylesheet">
<style>
  :root {
    --page: #e3e3e3;
    --paper: #f6f6f5;
    --orange: #e08b22;
    --ink: #4a4a4a;
    --ink-soft: #5c5c5c;
    --rule: #9a9a9a;
  }
  * { margin: 0; padding: 0; box-sizing: border-box; }
  html, body { width: 724px; height: 1200px; overflow: hidden; }
  body { background: var(--page); position: relative; font-family: "Bitter", serif; }

  .card {
    position: absolute;
    width: 480px;
    height: 274px;
    border-radius: 14px;
    background: var(--paper);
    box-shadow: 0 2px 6px rgba(0,0,0,0.12);
    overflow: hidden;
  }
  .card--front { left: 120px; top: 99px; }
  .card--slogan { left: 126px; top: 429px; background: var(--orange); }
  .card--appointment { left: 133px; top: 760px; }

  /* Front */
  .brand {
    position: absolute; left: 46px; top: 84px; width: 170px;
    color: var(--orange); font-family: "Bitter", serif; font-weight: 400;
  }
  .brand__name { display: block; font-size: 38px; line-height: 1; }
  .brand__line { display: block; font-size: 16px; letter-spacing: 3.5px; margin-top: 10px; text-transform: uppercase; line-height: 1.4; }
  .divider { position: absolute; left: 224px; top: 60px; width: 1px; height: 144px; background: var(--rule); }
  .contact { position: absolute; left: 240px; top: 58px; font-family: "Arimo", sans-serif; color: var(--ink); }
  .contact__name { font-size: 20px; font-weight: 700; color: var(--orange); line-height: 1.1; }
  .contact__role { font-size: 11px; color: var(--ink-soft); margin-top: 2px; }
  .contact__address { font-size: 13px; line-height: 17px; margin-top: 12px; }
  .contact__list { list-style: none; margin-top: 10px; font-size: 13px; line-height: 17px; }
  .contact__list li { display: flex; align-items: center; gap: 6px; }
  .contact__list svg { width: 11px; height: 11px; flex: none; }

  /* Slogan back */
  .slogan { position: absolute; inset: 0; display: flex; flex-direction: column; align-items: center; justify-content: center; color: #fff; text-align: center; padding-bottom: 20px; }
  .slogan__key { font-size: 56px; line-height: 1; font-weight: 400; }
  .slogan__rest { font-size: 22px; line-height: 23px; }

  /* Appointment back */
  .appointment__headline { position: absolute; left: 0; right: 0; top: 26px; text-align: center; }
  .appointment__key { display: block; font-size: 56px; line-height: 1; color: var(--orange); }
  .appointment__rest { display: block; font-size: 22px; line-height: 23px; color: var(--ink); }
  .appointment__band { position: absolute; left: 34px; width: 412px; top: 154px; height: 22px; background: var(--orange); color: #fff; text-align: center; font-size: 18px; line-height: 22px; letter-spacing: 0.5px; }
  .appointment__field { position: absolute; top: 198px; display: flex; align-items: flex-end; font-size: 15px; color: var(--ink-soft); }
  .appointment__field .line { display: block; border-bottom: 1px solid var(--ink-soft); margin-left: 3px; margin-bottom: 4px; }
  .field--date { left: 37px; }
  .field--date .line { width: 168px; }
  .field--time { left: 278px; }
  .field--time .line { width: 120px; }
  .appointment__url { position: absolute; left: 0; right: 0; top: 238px; text-align: center; font-size: 11px; letter-spacing: 1.2px; color: var(--ink); }
  .appointment__url em { font-style: normal; color: var(--orange); }
</style>
</head>
<body>

<section class="card card--front" aria-label="Business card front">
  <div class="brand">
    <span class="brand__name">Keystone</span>
    <span class="brand__line">Carpet +<br>Flooring</span>
  </div>
  <div class="divider"></div>
  <div class="contact">
    <p class="contact__name">Dan Reyes</p>
    <p class="contact__role">Project Manager + Lead Estimator</p>
    <p class="contact__address">1275 Harbor View Rd<br>Port Linden FL 34000</p>
    <ul class="contact__list">
      <li><svg viewBox="0 0 12 12" aria-hidden="true"><path d="M2.5 1 L4.5 1 L5.3 3.6 L4 4.6 Q5 7 7.4 8 L8.4 6.7 L11 7.5 L11 9.5 Q10.5 11 9 11 Q1 10 1 3 Q1 1.5 2.5 1 Z" fill="var(--orange)"/></svg>555.014.2290</li>
      <li><svg viewBox="0 0 12 12" aria-hidden="true"><rect x="1" y="2.5" width="10" height="7" fill="var(--orange)"/><path d="M1 2.5 L6 6.5 L11 2.5" fill="none" stroke="#fff" stroke-width="1"/></svg>dan@keystoneflooring.com</li>
      <li><svg viewBox="0 0 12 12" aria-hidden="true"><circle cx="6" cy="6" r="5" fill="var(--orange)"/><path d="M1 6 H11 M6 1 Q3 6 6 11 M6 1 Q9 6 6 11" fill="none" stroke="#fff" stroke-width="0.8"/></svg>www.keystoneflooring.com</li>
    </ul>
  </div>
</section>

<section class="card card--slogan" aria-label="Business card back with slogan">
  <div class="slogan">
    <span class="slogan__key">Keystone</span>
    <span class="slogan__rest">means doing<br>it right when no one<br>is looking</span>
  </div>
</section>

<section class="card card--appointment" aria-label="Business card back with appointment slot">
  <div class="appointment__headline">
    <span class="appointment__key">Keystone</span>
    <span class="appointment__rest">flooring at<br>an affordable price</span>
  </div>
  <div class="appointment__band">APPOINTMENT</div>
  <div class="appointment__field field--date">Date<span class="line"></span></div>
  <div class="appointment__field field--time">Time<span class="line"></span></div>
  <p class="appointment__url">www.<em>keystoneflooring</em>.com</p>
</section>

</body>
</html>
```